Brindle painting & waterproofing business card.

Business cards updated to reflect photos attached. we have given the photos of the old business cards and some of our updated designs for other items we have here in the office. Please see attached. if anyone needs to contact us directly for clarification you can email us at brindlerestoration@mailcove.example

Industry/Entity Type

Construction

Contact Information for Business Card

See attached photos

Font styles to use
Other font styles liked:
• Same as photos

Colors
ec1f27

Requirements
Must have
• Employee Names,
• Dennis Marlow II, Supervisor/Owner
• Dee Marlow, President/Owner
• Gus Tremby, Sales Representative
• Lyle Varsen, Supervisor
• Change 20 years to 25
Nice to have
• ideas reflecting the attached photos
Should not have
• should not be exactly like attached photos as those are old business card but reflect to match new logo listed as korvel van and cup photo.

```html
<!DOCTYPE html>
<html lang="en">
<head>
<meta charset="utf-8">
<title>Brindle's Painting &amp; Restoration – Business Card</title>
<link href="https://fonts.googleapis.com/css2?family=Roboto:wght@400;500;700;900&family=Roboto+Condensed:wght@500;700&family=Libre+Caslon+Text&display=swap" rel="stylesheet">
<style>
  :root {
    --brand-red: #ec1f27;
    --deep-red: #a3161c;
    --darkest-red: #86141a;
    --ink: #1c1c1c;
    --paper: #ffffff;
    --mist: #ececec;
    --stage: #8c8c8c;
  }
  * { margin: 0; padding: 0; box-sizing: border-box; }
  html, body { width: 1200px; height: 675px; overflow: hidden; }
  body {
    background: var(--stage);
    font-family: "Roboto", sans-serif;
    display: flex;
    align-items: center;
    justify-content: center;
    gap: 40px;
  }
  .card {
    position: relative;
    width: 540px;
    height: 308px;
    overflow: hidden;
    box-shadow: 0 6px 18px rgba(0,0,0,.35);
  }
  .card-backdrop { position: absolute; inset: 0; }

  /* Front */
  .card-front { background: var(--brand-red); color: var(--paper); }
  .front-logo {
    position: absolute; top: 22px; left: 0; right: 0;
    text-align: center; font-weight: 900; line-height: 1;
    text-transform: uppercase; color: var(--paper);
  }
  .front-logo .logo-name { font-size: 54px; letter-spacing: 2px; display: block; }
  .front-logo .logo-trade { font-size: 22px; letter-spacing: 3px; display: block; margin-top: 6px; }
  .front-tagline {
    position: absolute; top: 112px; left: 0; right: 0; text-align: center;
    font-family: "Roboto Condensed", sans-serif; font-weight: 700;
    font-size: 13px; letter-spacing: .5px;
  }
  .anniversary-mark {
    position: absolute; top: 136px; left: 205px; width: 130px; height: 80px;
    background: linear-gradient(135deg, rgba(255,255,255,.18), rgba(255,255,255,.06));
    border-radius: 4px;
  }
  .front-services {
    position: absolute; left: 0; right: 0; bottom: 26px; text-align: center;
    font-family: "Roboto Condensed", sans-serif; font-weight: 700;
    font-size: 13.5px; line-height: 1.55; text-transform: uppercase;
  }

  /* Back */
  .card-back { background: var(--paper); color: var(--ink); }
  .back-logo {
    position: absolute; top: 78px; left: 30px; width: 240px;
    text-align: center; font-weight: 900; line-height: 1;
    text-transform: uppercase; color: var(--brand-red);
  }
  .back-logo .logo-name { font-size: 40px; letter-spacing: 1px; display: block; }
  .back-logo .logo-trade { font-size: 15px; letter-spacing: 2px; display: block; margin-top: 5px; }
  .credentials {
    position: absolute; top: 180px; left: 30px; width: 240px; text-align: center;
    font-family: "Roboto Condensed", sans-serif; font-weight: 500;
    font-size: 15px; line-height: 1.25; text-transform: uppercase;
  }
  .divider {
    position: absolute; left: 290px; top: 38px; width: 1px; height: 168px;
    background: #3a3a3a;
  }
  .contact-block { position: absolute; left: 308px; top: 34px; width: 225px; }
  .contact-name {
    font-weight: 700; font-size: 30px; color: var(--brand-red);
    letter-spacing: .5px; line-height: 1;
  }
  .contact-title {
    font-weight: 500; font-size: 9.5px; letter-spacing: 3.2px;
    text-transform: uppercase; margin-top: 4px;
  }
  .contact-address { font-size: 11.5px; line-height: 1.35; margin-top: 10px; }
  .contact-lines { list-style: none; margin-top: 8px; font-size: 11.5px; line-height: 1.45; }
  .contact-lines li { display: flex; align-items: center; gap: 6px; white-space: nowrap; }
  .contact-lines svg { width: 10px; height: 10px; flex: none; fill: var(--brand-red); }
  .family-line {
    position: absolute; left: 250px; bottom: 28px;
    font-family: "Libre Caslon Text", serif; font-size: 16px; color: var(--ink);
  }
</style>
</head>
<body>

  <section class="card card-front" aria-label="Front of business card">
    <svg class="card-backdrop" viewBox="0 0 540 308" preserveAspectRatio="none" aria-hidden="true">
      <rect width="540" height="308" fill="var(--brand-red)"/>
      <path d="M0 118 C 150 150, 330 150, 540 120 L540 308 L0 308 Z" fill="var(--deep-red)"/>
      <path d="M0 210 C 160 190, 360 200, 540 250 L540 308 L0 308 Z" fill="var(--darkest-red)" opacity=".35"/>
    </svg>
    <div class="front-logo">
      <span class="logo-name">Brindle's</span>
      <span class="logo-trade">Painting &amp; Restoration</span>
    </div>
    <p class="front-tagline">SPECIALIZING IN HI-RISES &amp; COMMERCIAL</p>
    <div class="anniversary-mark" role="img" aria-label="Hand-lettered 'For over 25 years' anniversary mark"></div>
    <p class="front-services">
      • Painting • Waterproofing • Concrete Restoration • Electrostatic<br>
      • Expansion • Joints Caulking • Deck Coatings • Balustrades &amp; Railings
    </p>
  </section>

  <section class="card card-back" aria-label="Back of business card">
    <svg class="card-backdrop" viewBox="0 0 540 308" preserveAspectRatio="none" aria-hidden="true">
      <path d="M0 150 C 120 60, 260 20, 400 0 L460 0 C 300 40, 160 110, 0 210 Z" fill="var(--mist)"/>
      <path d="M0 250 C 140 190, 240 150, 330 110 L330 140 C 230 180, 120 230, 0 290 Z" fill="var(--mist)" opacity=".8"/>
      <path d="M150 308 C 200 250, 250 200, 300 170 C 260 210, 220 260, 190 308 Z" fill="var(--brand-red)"/>
      <path d="M420 308 C 460 250, 500 200, 540 180 L540 200 C 510 230, 480 270, 455 308 Z" fill="var(--brand-red)"/>
    </svg>
    <div class="back-logo">
      <span class="logo-name">Brindle's</span>
      <span class="logo-trade">Painting &amp; Restoration</span>
    </div>
    <p class="credentials">General Contractor<br>CGC#4830196<br>Licensed &amp; Insured</p>
    <div class="divider"></div>
    <div class="contact-block">
      <h1 class="contact-name">DEE MARLOW</h1>
      <p class="contact-title">President/Owner</p>
      <p class="contact-address">418 Harbor Reach Lane<br>Coral Vale, FL 33990</p>
      <ul class="contact-lines">
        <li><svg viewBox="0 0 10 10"><path d="M2 0.5 L3.6 2.6 L2.6 3.6 C3.2 5 4.8 6.6 6.4 7.2 L7.4 6.2 L9.5 7.8 L8.4 9.5 C4.5 9.3 0.7 5.5 0.5 1.6 Z"/></svg>555-214-0387</li>
        <li><svg viewBox="0 0 10 10"><path d="M2.5 0 H7.5 A1 1 0 0 1 8.5 1 V9 A1 1 0 0 1 7.5 10 H2.5 A1 1 0 0 1 1.5 9 V1 A1 1 0 0 1 2.5 0 Z M2.7 1.2 V8 H7.3 V1.2 Z"/></svg>555-306-7722</li>
        <li><svg viewBox="0 0 10 10"><path d="M0 2 H10 V8.5 H0 Z M0.8 2.6 L5 5.8 L9.2 2.6 V3.6 L5 6.8 L0.8 3.6 Z" fill-rule="evenodd"/></svg>brindlerestoration@mailcove.example</li>
        <li><svg viewBox="0 0 10 10"><circle cx="5" cy="5" r="4.3" fill="none" stroke="var(--brand-red)" stroke-width="1"/><path d="M0.7 5 H9.3 M5 0.7 V9.3" stroke="var(--brand-red)" stroke-width=".8" fill="none"/></svg>www.brindlerestoration.example</li>
      </ul>
    </div>
    <p class="family-line">Family Owned &amp; Opperated</p>
  </section>

</body>
</html>
```